project - Kestra Nook

Dear designers, I'm Looking for an appealing new business card design to represent us for our new e-cigarette store: The KestrA Nook. Knowledgeable and friendly staff we aim for superior customer service with a positive atmosphere. Classic feel with modern touch is what we are aiming for . Lime green font and grey back round is the original color scheme but we are flexible and open to suggestions. I added some doodles to show you where my mind is at. address: 4308 87 Ave NW Edmonton, AB (inside the hollin trade hall)web: thekestranook.com email: info@thekestranook.com phone : 587.555.0148 Thanks and am looking forward to seeing your creative , fresh and innovative designs.
Good luck everybody!
Jonas
lime green and charcoal grey please. thanks
Business
The KestrA Nook

```html
<!DOCTYPE html>
<html lang="en">
<head>
<meta charset="utf-8">
<title>Kestra Nook – Business Card</title>
<link rel="stylesheet" href="https://fonts.googleapis.com/css2?family=Open+Sans:wght@400;600;700;800&display=swap">
<style>
  :root{
    --page:#e4e4e2;
    --lime:#7cc242;
    --green:#3aa84a;
    --charcoal:#4a4a4c;
    --band-dark:#3b3b3d;
    --band-light:#8a8a8c;
    --card-white:#ffffff;
    --card-shade:#e6e6e6;
    --ink-light:#ffffff;
  }
  *{margin:0;padding:0;box-sizing:border-box}
  html,body{width:1200px;height:800px;overflow:hidden}
  body{
    background:var(--page);
    font-family:"Open Sans",Arial,sans-serif;
    display:flex;align-items:center;justify-content:center;gap:44px;
  }
  .card{
    position:relative;
    box-shadow:0 8px 24px rgba(0,0,0,.18);
    overflow:hidden;
  }
  .card-front{width:560px;height:320px;background:var(--card-white)}
  .card-back{
    width:320px;height:560px;
    background:radial-gradient(circle at 50% 45%,var(--card-white) 0%,var(--card-shade) 100%);
    display:flex;align-items:center;justify-content:center;
  }
  .front-shapes{position:absolute;inset:0}
  .contact{
    position:absolute;left:28px;top:26px;width:240px;color:var(--ink-light);
  }
  .contact-name{font-weight:700;font-size:16px;letter-spacing:.5px;text-transform:uppercase;line-height:1.2}
  .contact-title{font-size:12px;margin-top:2px}
  .contact-address{font-size:12px;line-height:1.55;margin-top:26px}
  .contact-lines{list-style:none;margin-top:34px;font-size:12px;line-height:1.75}
  .contact-lines li{display:flex;align-items:center;gap:9px}
  .contact-lines svg{width:11px;height:11px;flex:none}
  .brand-name{
    font-weight:800;color:var(--charcoal);text-transform:uppercase;
    line-height:.92;letter-spacing:-1px;
  }
  .front-brand{
    position:absolute;right:34px;top:118px;font-size:50px;text-align:left;
  }
  .back-brand{
    font-size:62px;white-space:nowrap;transform:rotate(90deg);
  }
</style>
</head>
<body>

  <section class="card card-front" aria-label="Card front">
    <svg class="front-shapes" viewBox="0 0 560 320" aria-hidden="true">
      <defs>
        <radialGradient id="greenGlow" cx="40%" cy="50%" r="65%">
          <stop offset="0" stop-color="#8ccd48"/>
          <stop offset="1" stop-color="#38a74a"/>
        </radialGradient>
        <linearGradient id="bandShade" x1="0" y1="0" x2="0" y2="1">
          <stop offset="0" stop-color="#2f2f31"/>
          <stop offset=".5" stop-color="#8a8a8c"/>
          <stop offset="1" stop-color="#3b3b3d"/>
        </linearGradient>
      </defs>
      <path d="M0 0H384Q238 160 318 320H0Z" fill="url(#bandShade)"/>
      <path d="M0 0H360Q214 160 296 320H0Z" fill="url(#greenGlow)"/>
    </svg>

    <div class="contact">
      <p class="contact-name">Marten Olsby</p>
      <p class="contact-title">Managing Director</p>
      <p class="contact-address">27 9th floor Hall<br>Ridgeway Road BVK</p>
      <ul class="contact-lines">
        <li><svg viewBox="0 0 12 12"><path d="M3 1l2 2.5-1.2 1.3c.7 1.5 1.8 2.6 3.3 3.3L8.4 6.9 11 9l-1.4 2C5 11 1 7 1 2.4Z" fill="currentColor"/></svg>012 555 0192</li>
        <li><svg viewBox="0 0 12 12"><circle cx="6" cy="6" r="5" fill="none" stroke="currentColor" stroke-width="1.3"/><circle cx="6" cy="6" r="2" fill="none" stroke="currentColor" stroke-width="1.3"/></svg>myname@inbox.com</li>
        <li><svg viewBox="0 0 12 12"><circle cx="6" cy="6" r="5" fill="none" stroke="currentColor" stroke-width="1.1"/><path d="M1 6h10M6 1c-2.5 3-2.5 7 0 10M6 1c2.5 3 2.5 7 0 10" fill="none" stroke="currentColor" stroke-width="1"/></svg>www.yoursitename.com</li>
      </ul>
    </div>

    <p class="brand-name front-brand">Kestra<br>Nook</p>
  </section>

  <section class="card card-back" aria-label="Card back">
    <p class="brand-name back-brand">Kestra Nook</p>
  </section>

</body>
</html>
```